Stationery and Business Card Design

We need stationary design for our new company pelvanta. Pelvanta is a company that provides city apartment rentals for tourists in Athens We need business cards, letterheads for A4 and A5 and envelopes for A4 A5. The design needs to be modern, friendly and corporate.

Target Market(s)

City Tourists

Industry/Entity Type

Tourism

```html
<!DOCTYPE html>
<html lang="en">
<head>
<meta charset="utf-8">
<title>Pelvanta Stationery</title>
<link rel="stylesheet" href="https://fonts.googleapis.com/css2?family=Open+Sans:wght@400;600;700&display=swap">
<style>
  :root {
    --brand: #8e0050;
    --ink: #2b2b2b;
    --charcoal: #3a3a3c;
    --paper: #ffffff;
    --board: #adadad;
    --rule: #9a9a9a;
  }
  * { margin: 0; padding: 0; box-sizing: border-box; }
  html, body { width: 1200px; height: 1200px; overflow: hidden; }
  body {
    background: var(--board);
    font-family: "Open Sans", Arial, sans-serif;
    color: var(--ink);
    position: relative;
  }
  .sheet {
    position: absolute;
    background: var(--paper);
    box-shadow: 3px 4px 6px rgba(0,0,0,0.35);
    overflow: hidden;
  }
  .brand-square { position: absolute; background: var(--brand); }
  .brand-name {
    position: absolute;
    color: var(--brand);
    font-weight: 400;
    white-space: nowrap;
    line-height: 1;
    letter-spacing: -0.01em;
  }

  /* Business card front */
  .card-front { left: 82px; top: 122px; width: 356px; height: 203px; }
  .card-front .person-name { position: absolute; left: 22px; top: 34px; font-size: 12px; font-weight: 700; color: var(--brand); }
  .card-front .person-role { position: absolute; left: 22px; top: 51px; font-size: 10.5px; }
  .card-front .title-rule { position: absolute; left: 70px; top: 57px; width: 160px; height: 1px; background: var(--brand); }
  .card-front .brand-square { left: 274px; top: 15px; width: 28px; height: 28px; }
  .card-front .brand-name { left: 240px; top: 46px; width: 97px; text-align: center; font-size: 18px; }
  .contact-list { position: absolute; left: 22px; top: 88px; list-style: none; font-size: 10.5px; }
  .contact-list li { display: flex; align-items: center; height: 16px; }
  .contact-list li.gap { margin-top: 4px; }
  .contact-list svg { width: 10px; height: 10px; margin-right: 8px; fill: none; stroke: var(--brand); stroke-width: 1.4; }
  .card-front .address { position: absolute; left: 22px; top: 158px; font-size: 10.5px; line-height: 13px; color: var(--brand); }

  /* Business card back */
  .card-back { left: 82px; top: 354px; width: 353px; height: 202px; }
  .card-back .brand-square { left: 145px; top: 43px; width: 59px; height: 59px; }
  .card-back .brand-name { left: 0; width: 353px; top: 112px; text-align: center; font-size: 40px; }

  /* Envelope front */
  .envelope-front { left: 51px; top: 594px; width: 520px; height: 260px; }
  .envelope-front .brand-square { left: 43px; top: 16px; width: 23px; height: 23px; }
  .envelope-front .brand-name { left: 14px; top: 45px; width: 81px; text-align: center; font-size: 14px; }
  .envelope-front .address { position: absolute; left: 16px; top: 232px; font-size: 6.5px; line-height: 8px; color: var(--brand); }

  /* Letterhead */
  .letterhead { left: 606px; top: 93px; width: 538px; height: 761px; }
  .letterhead .brand-square { left: 96px; top: 34px; width: 37px; height: 37px; }
  .letterhead .brand-name { left: 54px; top: 77px; width: 121px; text-align: center; font-size: 24px; }
  .letterhead .contact-block { position: absolute; left: 383px; top: 39px; height: 64px; border-left: 1px solid var(--brand); padding-left: 8px; font-size: 6.5px; line-height: 8px; }
  .letterhead .contact-block p { display: flex; align-items: center; white-space: nowrap; }
  .letterhead .contact-block svg { width: 6px; height: 6px; margin-right: 4px; fill: none; stroke: var(--brand); stroke-width: 1.6; }
  .letterhead .contact-block .spaced { margin-top: 11px; }
  .letterhead .contact-block .address { color: var(--brand); margin-top: 10px; }
  .letterhead .footer-rule { position: absolute; left: 0; bottom: 34px; width: 538px; height: 3px; background: var(--charcoal); }
  .letterhead .footer-band { position: absolute; left: 0; bottom: 0; width: 538px; height: 28px; background: var(--brand); }

  /* Envelope backs */
  .envelope-back { top: 887px; height: 261px; }
  .envelope-back.solid-flap { left: 51px; width: 522px; }
  .envelope-back.outline-flap { left: 614px; width: 524px; height: 262px; }
  .envelope-back .flap { position: absolute; left: 0; top: 0; width: 100%; height: 80px; }
  .envelope-back.solid-flap .flap-mark { position: absolute; left: 244px; top: 20px; width: 34px; height: 34px; background: var(--paper); }
  .envelope-back.outline-flap .brand-square { left: 246px; top: 22px; width: 32px; height: 32px; }
</style>
</head>
<body>

  <section class="sheet card-front" aria-label="Business card front">
    <p class="person-name">Marek Olsen</p>
    <p class="person-role">Director</p>
    <div class="title-rule"></div>
    <div class="brand-square"></div>
    <p class="brand-name">Pelvanta</p>
    <ul class="contact-list">
      <li><svg viewBox="0 0 10 10"><rect x="2.5" y="0.8" width="5" height="8.4" rx="0.8"/></svg>+1 555 014 2087</li>
      <li><svg viewBox="0 0 10 10"><path d="M7 1 C3 2 2 6 3 9"/></svg>+1 555 019 3341</li>
      <li class="gap"><svg viewBox="0 0 10 10"><rect x="0.8" y="2.5" width="8.4" height="6"/><path d="M0.8 2.5 L5 6 L9.2 2.5"/></svg>hello@pelvantastays.com</li>
      <li><svg viewBox="0 0 10 10"><circle cx="5" cy="5" r="4.2"/><path d="M0.8 5 H9.2 M5 0.8 C2.5 3 2.5 7 5 9.2 M5 0.8 C7.5 3 7.5 7 5 9.2"/></svg>www.pelvantastays.com</li>
    </ul>
    <p class="address">48 Harbor Lane, Suite 210<br>Brookdale, CA 95011</p>
  </section>

  <section class="sheet card-back" aria-label="Business card back">
    <div class="brand-square"></div>
    <p class="brand-name">Pelvanta</p>
  </section>

  <section class="sheet envelope-front" aria-label="Envelope front">
    <div class="brand-square"></div>
    <p class="brand-name">Pelvanta</p>
    <p class="address">48 Harbor Lane, Suite 210<br>Brookdale, CA 95011</p>
  </section>

  <section class="sheet letterhead" aria-label="Letterhead">
    <div class="brand-square"></div>
    <p class="brand-name">Pelvanta</p>
    <div class="contact-block">
      <p><svg viewBox="0 0 10 10"><path d="M7 1 C3 2 2 6 3 9"/></svg>+1 555 019 3341</p>
      <p class="spaced"><svg viewBox="0 0 10 10"><rect x="0.8" y="2.5" width="8.4" height="6"/><path d="M0.8 2.5 L5 6 L9.2 2.5"/></svg>hello@pelvantastays.com</p>
      <p><svg viewBox="0 0 10 10"><circle cx="5" cy="5" r="4.2"/><path d="M0.8 5 H9.2 M5 0.8 V9.2"/></svg>www.pelvantastays.com</p>
      <p class="address">48 Harbor Lane, Suite 210<br>Brookdale, CA 95011</p>
    </div>
    <div class="footer-rule"></div>
    <div class="footer-band"></div>
  </section>

  <section class="sheet envelope-back solid-flap" aria-label="Envelope back with coloured flap">
    <svg class="flap" viewBox="0 0 522 80" preserveAspectRatio="none" aria-hidden="true">
      <path d="M0 0 H522 C505 40 495 78 470 78 H52 C27 78 17 40 0 0 Z" fill="var(--brand)"/>
    </svg>
    <div class="flap-mark"></div>
  </section>

  <section class="sheet envelope-back outline-flap" aria-label="Envelope back with outlined flap">
    <svg class="flap" viewBox="0 0 524 80" preserveAspectRatio="none" aria-hidden="true">
      <path d="M0 0 C17 40 27 77 52 77 H472 C497 77 507 40 524 0" fill="none" stroke="var(--rule)" stroke-width="1"/>
    </svg>
    <div class="brand-square"></div>
  </section>

</body>
</html>
```